Crestline Lending Group Business Cards

We are looking to revamp the current business cards each of our locations uses. We are a lending company that specializes in personal loans, title loans, and tax services. We have locations in New Mexico, Texas, and Oklahoma.

We would like a cleaner, sleeker look while still highlighting what we offer. Title Loans, Personal Loans & Tax Services. We also want to include our referral fee somewhere on the card. We would like to see an English option as well as a Spanish option for the cards.

PLEASE NOTE: Some business cards do not include the employee's name but just the store's location, while others will include both.

These are double-sided business cards, and we would like to see proof if possible. I have included proofs of our current business cards for you to review below, as well as our company logo. Feel free to get creative with the logo, etc! Colors should match the logo; however, you do not need to use all of our logo colors if you don't want to.

```html
<!DOCTYPE html>
<html lang="es">
<head>
<meta charset="utf-8">
<title>Crestline Lending Group — Tarjetas de presentación</title>
<link href="https://fonts.googleapis.com/css2?family=Libre+Baskerville:wght@400;700&family=Montserrat:wght@300;400;800&family=Open+Sans:wght@600;700&family=Lato:wght@400;700&display=swap" rel="stylesheet">
<style>
  :root {
    --navy: #2b3a86;
    --teal: #107070;
    --green: #1d5a34;
    --ink: #222222;
    --paper: #ffffff;
    --page: #ffffff;
  }
  * { margin: 0; padding: 0; box-sizing: border-box; }
  html, body {
    width: 1200px; height: 480px; overflow: hidden;
    background: var(--page);
  }
  .sheet { position: relative; width: 1200px; height: 480px; }

  .card {
    position: absolute; top: 105px;
    width: 454px; height: 272px;
    background: var(--paper);
    box-shadow: 0 3px 6px rgba(0,0,0,0.22);
    overflow: hidden;
  }
  .card--front { left: 108px; }
  .card--back { left: 655px; }

  /* Front */
  .brand {
    position: absolute; left: 170px; top: 48px; width: 170px;
    display: flex; align-items: center; gap: 6px;
    font-family: "Open Sans", sans-serif; font-weight: 700;
    font-size: 12.5px; color: var(--green); white-space: nowrap;
  }
  .brand__dot { width: 9px; height: 9px; border-radius: 50%; background: var(--green); flex: none; }

  .section-label {
    position: absolute; height: 17px;
    font-family: "Libre Baskerville", serif; font-size: 10.5px;
    color: #fff; line-height: 17px; letter-spacing: 0.3px;
  }
  .section-label--services {
    left: 0; top: 87px; width: 272px; padding-left: 33px;
    background: linear-gradient(90deg, var(--navy) 0%, rgba(43,58,134,0.55) 50%, rgba(43,58,134,0) 100%);
  }
  .section-label--locations {
    right: 0; top: 129px; width: 145px; text-align: right; padding-right: 32px;
    font-weight: 700; font-size: 9px;
    background: linear-gradient(90deg, rgba(16,112,112,0) 0%, rgba(16,112,112,0.6) 40%, var(--teal) 100%);
  }

  .panel { position: absolute; left: 0; top: 0; }
  .services {
    position: absolute; left: 33px; top: 113px; list-style: none;
    font-family: "Open Sans", sans-serif; font-weight: 700;
    font-size: 16.5px; line-height: 20px; color: #fff;
  }
  .services li { display: flex; align-items: center; gap: 5px; }
  .services svg { width: 11px; height: 11px; flex: none; }

  .staff {
    position: absolute; right: 32px; top: 86px; text-align: right;
    font-family: "Lato", sans-serif; color: var(--ink);
  }
  .staff__name { font-weight: 700; font-size: 11.5px; letter-spacing: 0.2px; }
  .staff__role { font-size: 7.8px; margin-top: 1px; }

  .locations {
    position: absolute; right: 32px; top: 159px; list-style: none; text-align: right;
    font-family: "Open Sans", sans-serif; font-weight: 600;
    font-size: 11px; line-height: 14px; color: #fff;
  }
  .locations li::after {
    content: ""; display: inline-block; width: 4px; height: 4px; border-radius: 50%;
    background: #fff; margin-left: 5px; vertical-align: middle;
  }

  .contact {
    position: absolute; left: 33px; top: 197px; list-style: none;
    font-family: "Lato", sans-serif; font-size: 8.2px; color: var(--teal);
  }
  .contact li { display: flex; align-items: center; gap: 5px; height: 13.5px; }
  .contact svg { width: 9px; height: 9px; flex: none; }

  /* Back */
  .referral { position: absolute; inset: 0; text-align: center; font-family: "Montserrat", sans-serif; }
  .referral__lead {
    position: absolute; left: 0; right: 0; top: 62px;
    font-weight: 800; font-size: 30px; color: var(--teal); letter-spacing: 0.2px;
  }
  .referral__sub {
    position: absolute; left: 0; right: 0; top: 100px;
    font-weight: 300; font-size: 29px; color: var(--teal);
  }
  .referral__amount {
    position: absolute; left: 115px; top: 136px; width: 223px; height: 81px;
    background: var(--navy); color: #fff;
    font-weight: 800; font-size: 56px; line-height: 81px; letter-spacing: -1px;
  }
</style>
</head>
<body>
<main class="sheet">

  <section class="card card--front" aria-label="Frente de la tarjeta">
    <div class="brand"><span class="brand__dot"></span>Crestline Lending Group</div>

    <svg class="panel" width="454" height="272" viewBox="0 0 454 272" aria-hidden="true">
      <polygon points="0,111 342,111 385,184 0,184" fill="var(--navy)"/>
      <polygon points="303,154 454,154 454,207 326,207" fill="var(--teal)"/>
    </svg>

    <div class="section-label section-label--services">SERVICIOS</div>
    <ul class="services">
      <li><svg viewBox="0 0 12 12"><path d="M1 6.5 L4.5 10 L11 2" fill="none" stroke="#fff" stroke-width="1.4"/></svg>Préstamos Personales</li>
      <li><svg viewBox="0 0 12 12"><path d="M1 6.5 L4.5 10 L11 2" fill="none" stroke="#fff" stroke-width="1.4"/></svg>Préstamos sobre Títulos</li>
      <li><svg viewBox="0 0 12 12"><path d="M1 6.5 L4.5 10 L11 2" fill="none" stroke="#fff" stroke-width="1.4"/></svg>Servicios de Impuestos</li>
    </ul>

    <div class="staff">
      <div class="staff__name">LENA MARSH</div>
      <div class="staff__role">GERENTE DE SUCURSAL</div>
    </div>

    <div class="section-label section-label--locations">UBICACIONES:</div>
    <ul class="locations">
      <li>Nuevo México</li>
      <li>Oklahoma</li>
      <li>Texas</li>
    </ul>

    <ul class="contact">
      <li><svg viewBox="0 0 10 10"><circle cx="5" cy="5" r="4.4" fill="none" stroke="var(--teal)" stroke-width="0.8"/><path d="M3.3 2.8 L4.2 2.6 L4.6 3.8 L4 4.3 Q4.6 5.6 5.7 6 L6.2 5.4 L7.4 5.8 L7.2 6.7 Q5.8 7.3 4.1 5.9 Q2.8 4.5 3.3 2.8Z" fill="var(--teal)"/></svg>(505) 555-0148</li>
      <li><svg viewBox="0 0 10 10"><circle cx="5" cy="5" r="4.4" fill="none" stroke="var(--teal)" stroke-width="0.8"/><rect x="2.9" y="3.3" width="4.2" height="3.3" fill="var(--teal)"/></svg>servicios@crestlinelending.com</li>
      <li><svg viewBox="0 0 10 10"><circle cx="5" cy="5" r="4.4" fill="none" stroke="var(--teal)" stroke-width="0.8"/><path d="M5 2.2 a1.8 1.8 0 0 1 1.8 1.8 Q6.8 5.2 5 7.6 Q3.2 5.2 3.2 4 A1.8 1.8 0 0 1 5 2.2Z" fill="none" stroke="var(--teal)" stroke-width="0.8"/><circle cx="5" cy="4" r="0.6" fill="var(--teal)"/></svg>48 Mesa Verde Road, Suite B, Anytown, Texas 555</li>
    </ul>
  </section>

  <section class="card card--back" aria-label="Reverso de la tarjeta">
    <div class="referral">
      <p class="referral__lead">REFERIR A UN AMIGO Y</p>
      <p class="referral__sub">OBTENER HASTA</p>
      <p class="referral__amount">$100</p>
    </div>
  </section>

</main>
</body>
</html>
```